Vel-Trax.ch is looking for business card letterhead and envelope C5 with WOW effect

We need a strong business card for our company Vel-Trax.ch, logo is available. You want a black or dark background on which the logo Stark r% 26 # 252; appears. Letterhead and envelope in C5 format should be in a similar design, but does not have to be We need a strong business card for our company Vel-Trax.ch, logo is available. A black or dark background is desired, on which the logo Stark comes across. The letterhead and the envelope in C5 format should have a similar design.

Target Market(s)

Private customers as well as entrepreneurs

Contact Information for Business Card

E-mail: info@vel-trax.ch
Web.www.Vel-Trax.ch
Tel: +41 ( 0 ) 79 684 3027
Adresse:
Lindenhaldeweg 14
9412 Brenzikon

Hier kann man Icons verwenden für Email,Tel und Adressse

Font styles to use
Other font styles liked:
• Dubai,bold

Colors

Designer to choose colors to be used in the design.

Requirements
Must have
• WOW effect
Nice to have
• R% 26 # 252; back business card with our service listings. - VEHICLE LABELING - SHOP WINDOW LABELING - STICKERS AND MUCH MORE ... in red color

```html
<!DOCTYPE html>
<html lang="en">
<head>
<meta charset="utf-8">
<title>Vel-Trax.ch – Business Card</title>
<link rel="stylesheet" href="https://fonts.googleapis.com/css2?family=Exo+2:wght@600&family=Montserrat:wght@500;700&display=swap">
<style>
  :root {
    --backdrop: #8d5d38;
    --card: #1d1d1d;
    --accent: #fcc719;
    --text: #ffffff;
    --text-soft: #e9e9e9;
  }
  * { box-sizing: border-box; margin: 0; padding: 0; }
  html, body { width: 1200px; height: 700px; overflow: hidden; }
  body {
    background: var(--backdrop);
    font-family: "Montserrat", Arial, sans-serif;
    position: relative;
  }
  .card {
    position: absolute;
    width: 540px;
    height: 310px;
    background: var(--card);
    overflow: hidden;
    box-shadow: 0 6px 14px rgba(0,0,0,.35);
  }
  /* Front side */
  .card--front { left: 40px; top: 195px; }
  .front__pattern-area {
    position: absolute;
    left: 0; bottom: 0;
    width: 300px; height: 200px;
    background: linear-gradient(35deg, var(--accent) 0%, var(--accent) 45%, rgba(252,199,25,.55) 75%, rgba(252,199,25,0) 100%);
  }
  .front__brand {
    position: absolute;
    right: 34px; top: 42px;
    font-weight: 700;
    font-size: 34px;
    letter-spacing: 1px;
    color: var(--text);
  }
  .services {
    position: absolute;
    right: 30px; top: 96px;
    list-style: none;
    text-align: right;
  }
  .services li {
    font-weight: 500;
    font-size: 12.5px;
    letter-spacing: .5px;
    color: var(--text);
    line-height: 22px;
  }
  .services li::after {
    content: "";
    display: inline-block;
    width: 5px; height: 5px;
    border-radius: 50%;
    background: var(--accent);
    margin-left: 8px;
    vertical-align: 3px;
  }
  /* Back side */
  .card--back { left: 620px; top: 195px; }
  .back__brand {
    position: absolute;
    left: 60px; top: 140px;
    display: flex;
    align-items: center;
    gap: 12px;
  }
  .back__brand-dot {
    width: 22px; height: 22px;
    border-radius: 50%;
    background: var(--accent);
  }
  .back__brand-name {
    font-weight: 700;
    font-size: 21px;
    color: var(--text);
    letter-spacing: .5px;
  }
  .contact {
    position: absolute;
    left: 338px; top: 84px;
  }
  .contact__name {
    font-family: "Exo 2", "Montserrat", sans-serif;
    font-weight: 600;
    font-size: 21px;
    color: var(--accent);
  }
  .contact__role {
    font-weight: 500;
    font-size: 13px;
    color: var(--text-soft);
    margin-top: 2px;
  }
  .contact__address {
    font-style: normal;
    font-weight: 500;
    font-size: 12px;
    line-height: 15px;
    color: var(--text-soft);
    margin-top: 14px;
  }
  .contact__list { list-style: none; margin-top: 9px; }
  .contact__list li {
    display: flex;
    align-items: center;
    gap: 7px;
    font-weight: 500;
    font-size: 12px;
    line-height: 17px;
    color: var(--text-soft);
  }
  .contact__icon { width: 11px; height: 11px; fill: var(--accent); flex: none; }
</style>
</head>
<body>

  <section class="card card--front" aria-label="Business card front">
    <div class="front__pattern-area" role="img" aria-label="Yellow honeycomb pattern of large hexagons"></div>
    <div class="front__brand">VEL-TRAX.CH</div>
    <ul class="services">
      <li>VEHICLE LABELING</li>
      <li>SHOP WINDOW LABELING</li>
      <li>STICKERS</li>
    </ul>
  </section>

  <section class="card card--back" aria-label="Business card back">
    <div class="back__brand">
      <span class="back__brand-dot"></span>
      <span class="back__brand-name">VEL-TRAX.CH</span>
    </div>
    <div class="contact">
      <h1 class="contact__name">Daniel Keller</h1>
      <p class="contact__role">President</p>
      <address class="contact__address">Lindenhaldeweg 14<br>9412 Brenzikon</address>
      <ul class="contact__list">
        <li>
          <svg class="contact__icon" viewBox="0 0 24 24"><path d="M6.6 10.8a15.1 15.1 0 0 0 6.6 6.6l2.2-2.2c.3-.3.7-.4 1-.2 1.1.4 2.3.6 3.6.6.6 0 1 .4 1 1V20c0 .6-.4 1-1 1A17 17 0 0 1 3 4c0-.6.4-1 1-1h3.5c.6 0 1 .4 1 1 0 1.3.2 2.5.6 3.6.1.3 0 .7-.2 1z"/></svg>
          +41 ( 0 ) 79 684 3027
        </li>
        <li>
          <svg class="contact__icon" viewBox="0 0 24 24"><path d="M2 5h20v2l-10 6L2 7z"/><path d="M2 9l10 6 10-6v10H2z"/></svg>
          info@vel-trax.ch
        </li>
        <li>
          <svg class="contact__icon" viewBox="0 0 24 24"><circle cx="12" cy="12" r="10" fill="none" stroke="#fcc719" stroke-width="2.5"/><path d="M2 12h20M12 2c3 3 3 17 0 20M12 2c-3 3-3 17 0 20" fill="none" stroke="#fcc719" stroke-width="2"/></svg>
          www.Vel-Trax.ch
        </li>
      </ul>
    </div>
  </section>

</body>
</html>
```